Business Cards and Stationery for Consulting Firm
Harbor Crest Partners
Business Cards and Stationery for Consulting Firm - Consulting
Creative Brief
Professional
Ellis Thorne, PE, LEED AP
President
2738 Marwick Ln Ashford, VA 20817
ellis.thorne@harborcrestpartners-example.com
www.harborcrestpartners-example.com
We want a black background with only the logo. We want the logo to have a metallic finish on the back side only.
hcpadmin hcpadmin
Please make sure to use image file "31 HCP Revision" on the back of the business card, because we want the back of the business card to have a black background. Use image file "21 HCP Revision" when working with a white background.

```html
<!DOCTYPE html>
<html lang="en">
<head>
<meta charset="utf-8">
<title>Harbor Crest Partners — Stationery Concepts</title>
<link href="https://fonts.googleapis.com/css2?family=Arimo:ital,wght@0,400;0,700;1,400&family=Tinos&family=Allura&display=swap" rel="stylesheet">
<style>
:root{
  --board:#6e5a4a;
  --ink:#111111;
  --paper:#ffffff;
  --paper-shade:#efefef;
  --grey:#6f6f6f;
  --grey-light:#a9a9a9;
  --label:#f3ece4;
}
*{margin:0;padding:0;box-sizing:border-box}
html,body{width:1200px;height:247px;overflow:hidden;background:var(--board)}
.board{position:relative;width:1200px;height:247px;background:var(--board);font-family:Arimo,Arial,sans-serif;color:var(--ink)}
.piece{position:absolute;overflow:hidden}
.piece svg.shape{position:absolute;left:0;top:0;width:100%;height:100%}
.label{position:absolute;font-family:Tinos,"Times New Roman",serif;font-size:3.6px;color:var(--label);text-align:center}
.wordmark{position:absolute;font-weight:700;white-space:nowrap;letter-spacing:.02em;text-transform:uppercase}
.title-block .wordmark{left:70px;top:78px;font-size:7.2px;color:#1b1b1b}
.title-block .subtitle{position:absolute;left:70px;width:90px;top:95px;font-family:Tinos,"Times New Roman",serif;font-size:7px;color:var(--label);text-align:center}
.card{background:var(--paper);border-radius:2px}
.card .name{position:absolute;right:4px;top:4px;font-size:2.5px;font-weight:700;color:#fff;white-space:nowrap}
.card .role{position:absolute;right:4px;top:7.3px;font-size:1.8px;font-style:italic;color:#fff}
.card .wordmark{font-size:2.6px;color:var(--ink)}
.card .info{position:absolute;font-size:1.6px;line-height:2.3px;color:#222;white-space:nowrap}
.card .info .ico{display:inline-block;width:1.3px;height:1.3px;background:#222;border-radius:50%;margin-right:.6px;vertical-align:middle}
.card.back{background:var(--ink)}
.card.back .wordmark{left:0;right:0;top:24px;text-align:center;color:#fff;font-size:3px}
.sheet{background:var(--paper)}
.sheet .wordmark{font-size:2.7px}
.sheet .contact{position:absolute;font-size:1.7px;line-height:2.3px;color:#333;white-space:nowrap}
.sheet .letter{position:absolute;left:13px;right:14px;font-size:2.2px;line-height:2.9px;color:#555}
.sheet .letter strong{color:var(--ink)}
.sheet .letter p{margin-bottom:2.6px}
.sheet .sign{font-family:Allura,cursive;font-size:8px;color:#222;line-height:7px}
.sheet .footer{position:absolute;left:0;right:0;bottom:2.5px;font-size:1.6px;color:#fff;text-align:center;white-space:nowrap}
.flap-mark{position:absolute;left:0;right:0;text-align:center;font-size:2.8px;font-weight:700}
.folder-spine{position:absolute;font-size:1.5px;color:#fff;writing-mode:vertical-rl;white-space:nowrap}
</style>
</head>
<body>
<div class="board">

  <section class="title-block">
    <div class="wordmark">Harbor Crest Partners</div>
    <div class="subtitle">Stationary Concepts</div>
  </section>

  <!-- Business card fronts -->
  <article class="piece card" style="left:15px;top:114px;width:94px;height:53px">
    <svg class="shape" viewBox="0 0 94 53" preserveAspectRatio="none"><path d="M0 11C25 4 60 10 94 6V0H0Z" fill="#111"/><path d="M0 11C25 4 60 10 94 6V9C60 13 25 8 0 14Z" fill="#8a8a8a"/></svg>
    <div class="name">Ellis Thorne, PE, LEED AP</div><div class="role">President</div>
    <div class="wordmark" style="left:7px;top:24px">Harbor Crest Partners</div>
    <div class="info" style="left:7px;top:43px">2738 Marwick Ln<br>Ashford, VA 20817</div>
    <div class="info" style="left:50px;top:39px"><span class="ico"></span>410-555-0187<br><span class="ico"></span>ellis.thorne@harborcrestpartners-example.com<br><span class="ico"></span>www.harborcrestpartners-example.com</div>
  </article>
  <div class="label" style="left:15px;top:171px;width:94px">Front Card_Option_01</div>

  <article class="piece card" style="left:120px;top:114px;width:94px;height:53px">
    <svg class="shape" viewBox="0 0 94 53" preserveAspectRatio="none"><path d="M0 17C30 6 60 12 94 8V0H0Z" fill="#111"/><path d="M0 17C30 6 60 12 94 8V11C60 15 30 10 0 20Z" fill="#8a8a8a"/></svg>
    <div class="name">Ellis Thorne, PE, LEED AP</div><div class="role">President</div>
    <div class="wordmark" style="left:5px;top:39px;font-size:2.4px">Harbor Crest Partners</div>
    <div class="info" style="left:50px;top:25px">2738 Marwick Ln<br>Ashford, VA 20817</div>
    <div class="info" style="left:50px;top:32px"><span class="ico"></span>410-555-0187<br><span class="ico"></span>ellis.thorne@harborcrestpartners-example.com<br><span class="ico"></span>www.harborcrestpartners-example.com</div>
  </article>
  <div class="label" style="left:120px;top:171px;width:94px">Front Card_Option_02</div>

  <article class="piece card back" style="left:15px;top:181px;width:94px;height:53px">
    <div class="wordmark">Harbor Crest Partners</div>
  </article>
  <div class="label" style="left:15px;top:238px;width:94px">Back Card</div>

  <article class="piece card" style="left:120px;top:181px;width:94px;height:53px">
    <svg class="shape" viewBox="0 0 94 53" preserveAspectRatio="none"><path d="M0 17C30 6 60 12 94 20V0H0Z" fill="#111"/><path d="M0 17C30 6 60 12 94 20V23C60 15 30 10 0 20Z" fill="#8a8a8a"/></svg>
    <div class="name">Ellis Thorne, PE, LEED AP</div><div class="role">President</div>
    <div class="wordmark" style="left:5px;top:40px;font-size:2.4px">Harbor Crest Partners</div>
    <div class="info" style="left:50px;top:26px">2738 Marwick Ln<br>Ashford, VA 20817</div>
    <div class="info" style="left:50px;top:33px"><span class="ico"></span>410-555-0187<br><span class="ico"></span>ellis.thorne@harborcrestpartners-example.com<br><span class="ico"></span>www.harborcrestpartners-example.com</div>
  </article>
  <div class="label" style="left:120px;top:238px;width:94px">Front Card_Option_03</div>

  <!-- Letterhead option 01 -->
  <article class="piece sheet" style="left:221px;top:31px;width:158px;height:203px">
    <svg class="shape" viewBox="0 0 158 203" preserveAspectRatio="none"><path d="M0 188C40 172 80 196 120 182C140 175 150 172 158 170V203H0Z" fill="#111"/><path d="M0 184C40 168 80 192 120 178C140 171 150 168 158 166V170C150 172 140 175 120 182C80 196 40 172 0 188Z" fill="#8a8a8a"/></svg>
    <div class="wordmark" style="left:12px;top:21px">Harbor Crest Partners</div>
    <div class="contact" style="left:107px;top:9px">2738 Marwick Ln<br>Ashford, VA 20817<br>&#9742; 410-555-0187<br>&#9993; ellis.thorne@harborcrestpartners-example.com</div>
    <div class="letter" style="top:44px">
      <p>Date</p>
      <p><strong>Recipient Name</strong></p>
      <p>Company Name<br>Street Address<br>City, State, Zip</p>
      <p>Lorem ipsum dolor sit amet, consectetuer adipiscing elit, sed diam nonummy nibh euismod tincidunt ut laoreet dolore magna aliquam erat volutpat. Ut wisi enim ad minim veniam, quis nostrud exerci tation ullamcorper suscipit lobortis nisl ut aliquip ex ea commodo consequat.</p>
      <p>Nulla facilisis at vero eros et accumsan et iusto odio dignissim qui blandit praesent luptatum zzril delenit augue duis dolore te feugait nulla facilisi. Nam liber tempor cum soluta nobis eleifend option congue nihil imperdiet doming id quod mazim placerat facer possim assum.</p>
      <p>Legere me lius quod ii legunt saepius. Claritas est etiam processus dynamicus, qui sequitur mutationem consuetudium lectorum.</p>
      <p>Sincerely,</p>
      <div class="sign">Signature</div>
      <p><strong>Ellis Thorne, PE, LEED AP</strong><br>President</p>
    </div>
    <div class="footer" style="text-align:right;padding-right:8px">www.harborcrestpartners-example.com</div>
  </article>
  <div class="label" style="left:221px;top:238px;width:158px">Letterhead option_01</div>

  <!-- Letterhead option 02 -->
  <article class="piece sheet" style="left:389px;top:31px;width:158px;height:203px">
    <svg class="shape" viewBox="0 0 158 203" preserveAspectRatio="none"><path d="M0 182C40 178 70 196 110 188C135 182 150 178 158 176V203H0Z" fill="#111"/><path d="M0 178C40 174 70 192 110 184C135 178 150 174 158 172V176C150 178 135 182 110 188C70 196 40 178 0 182Z" fill="#8a8a8a"/></svg>
    <div class="wordmark" style="left:0;right:0;text-align:center;top:17px">Harbor Crest Partners</div>
    <div class="letter" style="top:36px">
      <p>Date</p>
      <p><strong>Recipient Name</strong></p>
      <p>Company Name<br>Street Address<br>City, State, Zip</p>
      <p>Lorem ipsum dolor sit amet, consectetuer adipiscing elit, sed diam nonummy nibh euismod tincidunt ut laoreet dolore magna aliquam erat volutpat. Ut wisi enim ad minim veniam, quis nostrud exerci tation ullamcorper suscipit lobortis nisl ut aliquip ex ea commodo consequat.</p>
      <p>Nulla facilisis at vero eros et accumsan et iusto odio dignissim qui blandit praesent luptatum zzril delenit augue duis dolore te feugait nulla facilisi. Nam liber tempor cum soluta nobis eleifend option congue nihil imperdiet doming id quod mazim placerat facer possim assum.</p>
      <p>Legere me lius quod ii legunt saepius. Claritas est etiam processus dynamicus, qui sequitur mutationem consuetudium lectorum.</p>
      <p>Sincerely,</p>
      <div class="sign">Signature</div>
      <p><strong>Ellis Thorne, PE, LEED AP</strong><br>President</p>
    </div>
    <div class="footer">2738 Marwick Ln, Ashford, VA 20817 &nbsp;P: 410-555-0187 &nbsp;E: ellis.thorne@harborcrestpartners-example.com &nbsp;W: www.harborcrestpartners-example.com</div>
  </article>
  <div class="label" style="left:389px;top:238px;width:158px">Letterhead option_02</div>

  <!-- Email signature -->
  <article class="piece card" style="left:592px;top:85px;width:105px;height:50px;border-radius:0">
    <svg class="shape" viewBox="0 0 105 50" preserveAspectRatio="none"><path d="M0 17C30 6 65 14 105 8V0H0Z" fill="#111"/><path d="M0 17C30 6 65 14 105 8V11C65 17 30 9 0 20Z" fill="#8a8a8a"/></svg>
    <div class="name">Ellis Thorne, PE, LEED AP</div><div class="role">President</div>
    <div class="wordmark" style="left:5px;top:35px;font-size:2.4px">Harbor Crest Partners</div>
    <div class="info" style="left:54px;top:23px">2738 Marwick Ln<br>Ashford, VA 20817</div>
    <div class="info" style="left:54px;top:30px"><span class="ico"></span>410-555-0187<br><span class="ico"></span>ellis.thorne@harborcrestpartners-example.com<br><span class="ico"></span>www.harborcrestpartners-example.com</div>
  </article>
  <div class="label" style="left:592px;top:141px;width:105px">Email Signature</div>

  <!-- Envelope front -->
  <article class="piece sheet" style="left:556px;top:160px;width:170px;height:74px">
    <svg class="shape" viewBox="0 0 170 74" preserveAspectRatio="none"><path d="M0 60C50 52 110 62 170 56V74H0Z" fill="#111"/><path d="M0 57C50 49 110 59 170 53V56C110 62 50 52 0 60Z" fill="#8a8a8a"/></svg>
    <div class="wordmark" style="left:8px;top:18px">Harbor Crest Partners</div>
    <div class="contact" style="left:7px;top:23px">2738 Marwick Ln, Ashford, VA 20817</div>
  </article>
  <div class="label" style="left:556px;top:238px;width:170px">Envelope_Front</div>

  <!-- Envelope backs -->
  <article class="piece" style="left:755px;top:80px;width:167px;height:75px;background:var(--paper-shade)">
    <svg class="shape" viewBox="0 0 167 75" preserveAspectRatio="none"><path d="M0 0H167V20Q167 24 163 25H4Q0 24 0 20Z" fill="#111"/></svg>
    <div class="flap-mark" style="top:10px;color:#fff">HCP</div>
  </article>
  <article class="piece" style="left:745px;top:120px;width:167px;height:75px;background:var(--paper-shade)">
    <svg class="shape" viewBox="0 0 167 75" preserveAspectRatio="none"><path d="M0 0H167V20Q167 24 163 25H4Q0 24 0 20Z" fill="var(--grey)"/></svg>
    <div class="flap-mark" style="top:10px;color:#fff">HCP</div>
  </article>
  <article class="piece" style="left:733px;top:160px;width:170px;height:74px;background:var(--paper)">
    <svg class="shape" viewBox="0 0 170 74" preserveAspectRatio="none"><path d="M0 74L85 34L170 74" fill="none" stroke="#ddd" stroke-width=".6"/><path d="M0 0H170V18Q170 22 166 23H4Q0 22 0 18Z" fill="#f4f4f4" stroke="#ddd" stroke-width=".4"/></svg>
    <div class="flap-mark" style="top:10px;color:var(--ink)">HCP</div>
  </article>
  <div class="label" style="left:733px;top:238px;width:170px">Envelope_Back</div>

  <!-- Folder -->
  <article class="piece" style="left:936px;top:36px;width:250px;height:200px;overflow:visible">
    <div style="position:absolute;left:0;top:0;width:17px;height:146px;background:var(--grey)"></div>
    <div class="folder-spine" style="left:8px;top:22px">www.harborcrestpartners-example.com</div>
    <div style="position:absolute;left:17px;top:0;width:108px;height:200px;background:var(--ink)"></div>
    <div class="contact" style="position:absolute;left:23px;top:122px;font-size:1.6px;line-height:2.2px;color:#fff;white-space:nowrap">2738 Marwick Ln<br>Ashford, VA 20817<br>410-555-0187<br>ellis.thorne@harborcrestpartners-example.com</div>
    <div style="position:absolute;left:125px;top:0;width:118px;height:146px;background:var(--paper)"></div>
    <div class="wordmark" style="left:125px;width:118px;text-align:center;top:83px;font-size:5px;color:var(--ink)">Harbor Crest Partners</div>
    <div style="position:absolute;left:243px;top:0;width:7px;height:146px;background:var(--grey-light)"></div>
    <div style="position:absolute;left:125px;top:146px;width:108px;height:54px;background:var(--ink)"></div>
    <div style="position:absolute;left:162px;top:172px;width:47px;height:21px;background:var(--paper);transform:rotate(-12deg);border-radius:1px">
      <div class="wordmark" style="left:4px;top:10px;font-size:1.5px">Harbor Crest Partners</div>
      <div style="position:absolute;left:26px;top:3px;font-size:1.3px;line-height:1.8px;color:#222;white-space:nowrap">Ellis Thorne, PE, LEED AP<br>President<br>410-555-0187</div>
    </div>
  </article>
  <div class="label" style="left:1061px;top:238px;width:108px">Folder</div>

</div>
</body>
</html>
```